Wordpress Design Project - Executive Mentor Nexus

Website Brief

We are looking to have a design produced for a modern professional website. A mind map of the site can be found here: http://www.plotvine.example/view.htm?m=48120573b331498c97f2a1d6c0bb7f30

Each of the green tabs are pages just next to them is a very small green globe. If you click this. It will take you through to an example page for that section.

Task description
The website will be made up of:
1. A homepage (this will be the blog see http://www.tessawinbury.example for an example of the crisp and cleanness we are looking for)
2. A page that will have just a video and option page (see: http://qvlnacademy.example/ for example)
3. 3 pages all with the same structure. (see: http://qvlnacademy.example/zp27gkt93wqe/ for an example). Each will have:
a. A video
b. Tabs at the top of the video that link to the 3 videos and the sales page
c. Link to a resource download
d. Facebook Comments section
4. 2 Page with about the experts and about our company (same style for both)
5. A page that will have a long well designed sales page (see: http://qvlnacademy.example/early-enrollment-2013/ for an example)
6. A page with testimonials on it (see http://www.tessawinbury.example/praise/)
7. A page that will describe the products, services and provision we will be offering
8. A page that will detail our involvement with charities and not for profits

Must Have
Edgey, crisp design, similar to Tessa Winburys. We would like the colours to match very well throughout the site and have a unique font (possibly manksans). We want it to have very clean integrations between copy and images with shadows on videos for example like with Tessawinburys page. We really love this design and would like this to be the inspiration for our site however it would need to certainly have a more executive feel to suit our target market.

We like the idea of some kind of circles, crisp clean lines, nice white space, simple design, corporate looking, communicates wealth/success/massive value. Based on the two logos of GTPLA and the Hub (see attached)

Target Market:
The target market includes intelligent, productive coaches, who are self employed or part of small firms. They are well educated, well read, socially conscious, and committed to making a profound difference with their clients...skilled at the actions of coaching, but not the business side. There will be a ratio of approximately 60% male / 40% female (really? The coaching industry is predominantly female, no?), with an age range of 40 to 60 years. English is our core language. Most will have secondary education and the salary range will be $90,000 to $400,000. We will have a global audience reach, although the primary markets will be North America, Europe and Australia/NZ.

Marketing Objective:
EMN will be an on-line resource for Executive Coaches. The intent of the design will be to present EMN to the world as a highly professional organization. The intent is not to characterize EMN as solely corporate, but will also incorporate elements of entrepreneurialism. We require the brand to incorporate these values:
• Trustworthy – you can trust us
• Professional – we are true professionals whose mission is to provide value to our clients
• Caring - Interested in our clients wellbeing – we are keenly interested in helping our clients build their knowledge, skills, and attitudes to be highly productive and successful
• Successful
• Knowledgeable – we have breadth and depth of knowledge in leadership
• World-class – we have a world-wide target market and, as such, need the brand to reflect a powerful and inclusive image
• Positive Energy - I would like the brand to have positive energy and very clean feng shui
• Prestige
• Massive Value
• Accessible
• Worldly/ Sophisticated
• Affordable
• Mission-critical

Details about the needs, wants, aspirations etc. of our target market
Executive coaches need a process and a system for creating opportunities to do the work they love with clients who are qualified to engage them and pay them. There is a scarcity mentality around their own finances, but ironically an abundance mentality for what's possible in the world and for their clients. They want to make a difference, they want to facilitate transformation, they want to be of deep service.

They aspire to make a decent living doing it! They need help bridging the gap between practitioner/service provider and financially successful entrepreneur/business owner/ leader. They also aspire to have it be easy, as it feels hard for them to generate the revenues they want to generate solely through coaching, so many turn to training, speaking, and other revenue streams.

Required assets to send through to web designer
1. Three blog posts. Each will have:
a. A video/audio
b. Summary of the points raised
c. Download (possibly slides)
2. A page that will have just a video and option page
a. Headline
b. Video
c. One paragraph summary of what we do
3. 3 launch videos. Here for each we will need
a. A video scripted and produced
b. Title for each
c. A resource download
4. Sales page
a. Video
b. Copy
i. Overview
ii. Content of course
iii. Guarentee
iv. Details of bonuses
v. Details of support
vi. Pricing broken down ($30,000 value = $2000)
c. Animated Gif
5. About the company and experts
a. Description of our company, it's vision, mission, purpose and core values.
b. Description of each of us,
i. our key facts and wows,
ii. a picture of us
iii. some interesting facts (giving personality)
iv. Lower down we will add in "Faculty" these will be any thought leaders we invite in to be part of the value delivery (will add to our credibility having such a strong team behind the project)
6. Testimonials
a. Testimonials from coaches from working with us
7. Products, services and provision we will be offering
a. A simple description of each of the key products/services we will be offering
i. Executive Mentor Sales
ii. Executive Mentor Marketing
iii. Executive Mentor Help
iv. Executive Mentor Mastermind
v. Executive Mentor Resources
a. List of the various charity work each of us have been involved with

Requirements
Must have
• Edgey, crisp design, similar to Tessa Winburys. We would like the colours to match very well throughout the site and have a unique font (possibly manksans). We want it to have very clean integrations between copy and images with shadows on videos for example like with Tessawinburys page. We really love this design and would like this to be the inspiration for our site however it would need to certainly have a more executive feel to suit our target market.

```html
<!DOCTYPE html>
<html lang="en">
<head>
<meta charset="utf-8">
<title>Executive Mentor Nexus</title>
<link href="https://fonts.googleapis.com/css2?family=Montserrat:wght@500;600&family=Mada:wght@400;500&family=Roboto+Slab:wght@300;400&display=swap" rel="stylesheet">
<style>
  :root {
    --orange: #f07a1a;
    --orange-deep: #e5561a;
    --orange-light: #f7931e;
    --charcoal: #3f4042;
    --slate: #56585a;
    --grey-text: #6f6f6f;
    --nav-text: #6a6a6a;
    --header-bg: #f1f1f1;
    --white: #ffffff;
    --green: #3aa23a;
    --green-light: #6cc24a;
    --rule: #f3c7b0;
  }
  * { margin: 0; padding: 0; box-sizing: border-box; }
  html, body { width: 1200px; height: 847px; overflow: hidden; background: var(--white); }
  body { position: relative; font-family: "Mada", sans-serif; }

  .top-strip { position: absolute; left: 0; top: 0; width: 1200px; height: 6px; background: #48494b; }

  .site-header {
    position: absolute; left: 0; top: 6px; width: 1200px; height: 130px;
    background: linear-gradient(#f7f7f7, #ececec);
    box-shadow: 0 4px 10px rgba(0,0,0,.18); z-index: 3;
  }
  .brand { position: absolute; left: 107px; top: 40px; display: flex; flex-direction: column; align-items: center; gap: 14px; }
  .brand-mark { width: 22px; height: 22px; border-radius: 50%; background: var(--orange); }
  .brand-name { font-family: "Mada", sans-serif; font-size: 15px; font-weight: 400; color: var(--grey-text); letter-spacing: .1px; }

  .main-nav { position: absolute; left: 396px; top: 52px; display: flex; align-items: center; }
  .main-nav a {
    font-family: "Roboto Slab", serif; font-weight: 300; font-size: 12.5px; color: var(--nav-text);
    text-decoration: none; text-transform: uppercase; padding: 6px 23px 10px; position: relative;
  }
  .main-nav a + a { border-left: 1px solid #d6d6d6; }
  .main-nav a.is-active::after {
    content: ""; position: absolute; left: 14px; right: 22px; bottom: -4px; height: 4px; background: var(--orange);
  }

  .hero-photo {
    position: absolute; left: 0; top: 136px; width: 1200px; height: 500px;
    background: radial-gradient(ellipse at 72% 40%, #c9a58f 0%, #a6a4a2 28%, #8aa4c4 55%, #6f7276 80%, #3c3d3f 100%);
  }
  .hero-panel {
    position: absolute; left: -10px; top: 243px; width: 556px; height: 196px;
    background: rgba(70,70,72,.9); border: 4px solid rgba(220,220,220,.85);
    border-radius: 0 100px 100px 0; z-index: 2;
  }
  .hero-title {
    position: absolute; left: 106px; top: 262px; font-family: "Montserrat", sans-serif; font-weight: 600;
    font-size: 28px; line-height: 32px; letter-spacing: 1px; color: var(--orange-light); text-transform: uppercase; z-index: 2;
  }
  .hero-text { position: absolute; left: 106px; top: 332px; width: 360px; font-size: 14.5px; line-height: 20px; color: var(--white); z-index: 2; }
  .btn-learn {
    position: absolute; left: 106px; top: 384px; width: 151px; height: 39px; border-radius: 20px;
    border: 4px solid #b9b9b9; background: linear-gradient(#f9a23a, var(--orange-deep) 60%, #d44614);
    color: var(--white); font-family: "Roboto Slab", serif; font-size: 12px; text-align: center; line-height: 31px; z-index: 2;
  }

  .signup-band { position: absolute; left: 0; top: 565px; width: 1200px; height: 180px; }
  .signup-line {
    position: absolute; left: 106px; top: 630px; font-family: "Montserrat", sans-serif; font-weight: 500;
    font-size: 19px; color: var(--white); text-transform: uppercase; letter-spacing: .3px;
  }
  .field {
    position: absolute; top: 629px; width: 152px; height: 25px; background: var(--white); border-radius: 3px;
    font-family: "Roboto Slab", serif; font-size: 12px; color: #555; padding: 5px 12px;
  }
  .field-name { left: 610px; }
  .field-email { left: 776px; }
  .btn-signup {
    position: absolute; left: 944px; top: 622px; width: 150px; height: 39px; border-radius: 20px;
    border: 4px solid var(--white); background: linear-gradient(var(--green-light), var(--green));
    color: var(--white); font-family: "Roboto Slab", serif; font-size: 12px; text-align: center; line-height: 31px;
  }

  .content-sheet {
    position: absolute; left: 72px; top: 684px; width: 1054px; height: 200px; background: var(--white);
    box-shadow: 0 0 10px rgba(0,0,0,.15);
  }
  .post-title {
    position: absolute; left: 106px; top: 729px; width: 611px; height: 46px; background: linear-gradient(#2f3032, #3e3f41);
    color: var(--white); font-family: "Montserrat", sans-serif; font-weight: 500; font-size: 23px; padding: 10px 24px;
  }
  .post-media {
    position: absolute; left: 106px; top: 783px; width: 611px; height: 70px;
    background: linear-gradient(90deg, #e7e3df, #c9c0b6 40%, #d8d6d3);
  }
  .comment-flag {
    position: absolute; left: 97px; top: 782px; width: 93px; height: 28px; background: var(--orange-light);
    clip-path: polygon(0 0, 100% 0, 88% 50%, 100% 100%, 0 100%);
    color: var(--white); font-family: "Montserrat", sans-serif; font-size: 12px; font-weight: 600; padding: 6px 14px;
  }
  .comment-flag small { font-size: 7px; }

  .recent-heading {
    position: absolute; left: 764px; top: 730px; width: 324px; padding-bottom: 4px; border-bottom: 1px solid var(--rule);
    font-family: "Montserrat", sans-serif; font-weight: 600; font-size: 15px; color: var(--orange); letter-spacing: .3px;
  }
  .recent-item { position: absolute; left: 764px; width: 324px; font-size: 15px; line-height: 20px; color: var(--grey-text); }
</style>
</head>
<body>
  <div class="top-strip"></div>

  <header class="site-header">
    <div class="brand">
      <span class="brand-mark"></span>
      <span class="brand-name">ExecutiveMentorNexus.com</span>
    </div>
    <nav class="main-nav">
      <a class="is-active">Executive Mentor Marketing</a>
      <a>About</a>
      <a>Work With Us</a>
      <a>Giving Back</a>
      <a>Testimonials</a>
    </nav>
  </header>

  <div class="hero-photo" role="img" aria-label="Smiling senior executive in a light blue shirt"></div>
  <div class="hero-panel"></div>
  <h1 class="hero-title">Executive Mentor<br>Marketing</h1>
  <p class="hero-text">Lorem ipsum dolor sit amet, consectetuer adipiscing elit, sed diam nonunibh euismod tincidunt ut.</p>
  <div class="btn-learn">LEARN MORE</div>

  <svg class="signup-band" viewBox="0 0 1200 180" aria-hidden="true">
    <defs>
      <linearGradient id="bandFill" x1="0" y1="0" x2="0" y2="1">
        <stop offset="0" stop-color="#f3801e"/>
        <stop offset="1" stop-color="#e4501c"/>
      </linearGradient>
    </defs>
    <path d="M0 60 Q600 -20 1200 60 L1200 180 L0 180 Z" fill="url(#bandFill)"/>
    <path d="M0 60 Q600 -20 1200 60" fill="none" stroke="#ffffff" stroke-width="5"/>
  </svg>
  <p class="signup-line">Lorem ipsum dolor sit amet, consectetuer.</p>
  <div class="field field-name">First Name</div>
  <div class="field field-email">Email</div>
  <div class="btn-signup">SIGN UP TODAY</div>

  <main class="content-sheet"></main>
  <h2 class="post-title">LOREM IPSUM DOLOR SIT</h2>
  <div class="post-media" role="img" aria-label="Businesswoman with glasses in a bright office"></div>
  <div class="comment-flag">60 <small>COMMENTS</small></div>

  <h3 class="recent-heading">MOST RECENT POSTS</h3>
  <p class="recent-item" style="top:770px">Lorem ipsum dolor sit amet, consectetuer adipis cing elit, sed diam nonunibh euismod.</p>
  <p class="recent-item" style="top:829px">Lorem ipsum dolor sit amet, consectetuer adipis</p>
</body>
</html>
```